Popup Nightclub Grand Opening Flyer

We need to design a flyer for the grand opening of an upscale, exclusive nightclub called "Lanternfall". The design needs to be chic and exclusive. The background should be black and the text should primarily be white. We like minimalist designs.

Here is the text for the flyer
-
Velvetroom Atlanta Presents

Lanternfall (LOGO)

A Popup Nightclub Experience
For one night Only

Friday, October 18, 2013
Party begins at 9PM

INVITE ONLY

See invitation for location details
(Velvetroom Atlanta logo)

-
Examples we like

http://cdn2-b.plorvex-news.test/sites/default/files/styles/image_content_width/hash/3d/fb/4729105836_5521_flyer.jpg?itok=Q8rmZt2w

http://api.trevlomesh.test/files/9Kxq-Tr72PQd0hzXbwaLr8VMN2K617J3nqBw5CHR4XtdM8Y2sqEA-KjuxBnRoLW4QTyMHD8nwfYcJz-Rkh3vqp4MNaTYe9s1/7zenFridays.jpg

http://brenquist.test/wp-content/uploads/yootheme/widgetkit/gallery/7zen/7zen-gen_nvibe4-01.jpg
Updates

Hi All, one thing that we are seeing that we don't like is on over emphasis on the phrase "a popup nightclub experience" please don't make this the largest thing on the flyer

Target Market(s)

Target market is 25-35 year olds who are affluent (rich) and like luxury brands

Requirements
Must have
• Dark Background
Nice to have
• Velvetroom Logo on the bottom
Modern text that isn't curvy
Should not have
• Curved text

```html
<!DOCTYPE html>
<html lang="en">
<head>
<meta charset="utf-8">
<title>Lanternfall Nightclub – Velvetroom Atlanta</title>
<link rel="stylesheet" href="https://fonts.googleapis.com/css2?family=Josefin+Sans:wght@300&family=Open+Sans:wght@400;600;700&display=swap">
<style>
  :root {
    --night: #0b0b0c;
    --weave-light: #26272a;
    --weave-dark: #050506;
    --mint: #56e69a;
    --white: #ffffff;
    --silver: #c9cacc;
  }
  html, body {
    margin: 0;
    padding: 0;
    width: 851px;
    height: 1200px;
    overflow: hidden;
    background: var(--night);
  }
  .flyer {
    position: relative;
    width: 851px;
    height: 1200px;
    overflow: hidden;
    color: var(--white);
    font-family: "Open Sans", Arial, sans-serif;
  }
  .texture {
    position: absolute;
    inset: 0;
    background: radial-gradient(ellipse at 50% 40%, var(--weave-light) 0%, var(--night) 60%, var(--weave-dark) 100%);
  }
  .line {
    position: absolute;
    left: 0;
    width: 100%;
    margin: 0;
    text-align: center;
  }
  .presenter {
    top: 80px;
    font-size: 29px;
    font-weight: 400;
  }
  .band {
    position: absolute;
    left: 112px;
    width: 621px;
    background: var(--mint);
  }
  .band--top { top: 154px; height: 55px; }
  .band--bottom { top: 596px; height: 52px; }
  .mark {
    position: absolute;
    left: 376px;
    top: 268px;
  }
  .club-name {
    top: 462px;
    font-family: "Josefin Sans", "Helvetica Neue", sans-serif;
    font-weight: 300;
    font-size: 66px;
    letter-spacing: 7px;
    line-height: 1;
  }
  .club-type {
    top: 548px;
    font-family: "Josefin Sans", "Helvetica Neue", sans-serif;
    font-weight: 300;
    font-size: 30px;
    letter-spacing: 5px;
    line-height: 1;
  }
  .tagline {
    top: 662px;
    font-size: 16px;
    font-weight: 700;
    letter-spacing: 2.6px;
    word-spacing: 2px;
  }
  .date {
    font-size: 17px;
    font-weight: 400;
    letter-spacing: 6px;
    line-height: 1;
  }
  .date--day { top: 766px; }
  .date--time { top: 798px; }
  .notice {
    font-family: Arial, "Open Sans", sans-serif;
    font-size: 18px;
  }
  .notice--invite { top: 883px; }
  .notice--location { top: 925px; }
  .host-name {
    top: 990px;
    font-size: 44px;
    font-weight: 700;
    letter-spacing: 5px;
    line-height: 1;
  }
</style>
</head>
<body>
  <main class="flyer">
    <div class="texture" role="img" aria-label="Black woven carbon fibre texture"></div>

    <p class="line presenter">Velvetroom Atlanta Presents</p>

    <div class="band band--top"></div>

    <svg class="mark" width="100" height="100" viewBox="0 0 100 100" aria-hidden="true">
      <circle cx="50" cy="50" r="48" fill="var(--silver)"/>
    </svg>

    <p class="line club-name">LANTERNFALL</p>
    <p class="line club-type">NIGHTCLUB</p>

    <div class="band band--bottom"></div>

    <p class="line tagline">A Popup Nightclub Experience&nbsp; For one night Only</p>

    <p class="line date date--day">FRIDAY, OCTOBER&nbsp; 18, 2013</p>
    <p class="line date date--time">PARTY BEGINS AT 9PM</p>

    <p class="line notice notice--invite">Invite Only</p>
    <p class="line notice notice--location">See invitation for location details</p>

    <p class="line host-name">VELVETROOM ATLANTA</p>
  </main>
</body>
</html>
```